www.DeliaBrunwick.com

I am looking to redesign my author website. I want it to reflect my personality but look more professional AND more marketing savvy.

I am looking for:
- a header/banner with JUST MY NAME:
Delia Brunwick

- a header/banner using my name and log line - like this:
Delia Brunwick
Professional Writer. Amateur Mom.

- And a logo using my name and a different log line:
Delia Brunwick
Finding the funny in parenthood before somebody loses an eye.

- social media buttons for Drovely, Quenlo, Brimsetta, vostraloom, Tarvio +.

Regarding the design style I want to use the attached design for the basis of the website. I would like to use the logo in the UPPER RIGHT HAND CORNER of the four designs attached. It is the design with the slate blue background and yellowish/orangish colors.

I LOVE the typewriter font and would like to use that for my column headers - ideally, I would love it if when you roll over the headers it looks like they are being typed out - but I don't know if that is possible. If it isn't, happy just just get the headers in that font.

Target Market(s)

30-50 year old parents and educators. My target audience is educated with a great sense of style and sense of humor.

Industry/Entity Type

Marketing

Requirements
Must have
• - Clear, bold, client friendly design/buttons
- Professional, web-savvy design
- Modern/RETRO look
- Headers for the following verticals:
About Me
Books
Articles
TV
Hire Me
Speaking
Consulting
Classes
School Visits
Press
Blaaaahhhhg! (Blog)
Contact Me

```html
<!DOCTYPE html>
<html lang="en">
<head>
<meta charset="utf-8">
<title>Delia Brunwick – Professional Writer. Amateur Mom.</title>
<link href="https://fonts.googleapis.com/css2?family=Handlee&family=Questrial&display=swap" rel="stylesheet">
<style>
:root{
  --teal:#2f9aa3;
  --teal-light:#55b9c1;
  --teal-text:#3aa3ab;
  --orange:#f5a800;
  --orange-text:#f0a21a;
  --ink:#555;
  --body:#666;
  --link:#2a6fd6;
  --panel:#fff;
  --line:#dcdcdc;
  --page:#fff;
}
*{box-sizing:border-box;margin:0;padding:0}
html,body{width:1200px;height:1056px;overflow:hidden;background:var(--page)}
body{position:relative;font-family:Arial,Helvetica,sans-serif;color:var(--body)}
.hand{font-family:'Handlee',cursive}
.top-band{position:absolute;left:0;top:0;width:1200px;height:125px;background:linear-gradient(180deg,var(--teal) 0%,var(--teal-light) 100%)}
.brand{position:absolute;right:257px;top:34px;text-align:right;color:#fff}
.brand-name{font-family:'Handlee',cursive;font-size:42px;line-height:46px}
.brand-line{font-family:'Questrial',sans-serif;font-size:10px;letter-spacing:1px;margin-top:2px}
.panel{position:absolute;background:var(--panel);border:1px solid var(--line);border-radius:6px;box-shadow:0 6px 8px -4px rgba(0,0,0,.25)}
.main-nav{left:277px;top:10px;width:160px;height:268px;padding:16px 24px 0}
.main-nav a{display:block;font-family:'Handlee',cursive;font-size:13px;color:var(--teal-text);text-decoration:none;height:20px;line-height:20px;border-bottom:1px solid #eee}
.main-nav a.current{color:#555}
.share-note{position:absolute;left:277px;top:296px;width:160px;text-align:center;font-family:'Handlee',cursive;font-size:12px;line-height:19px;color:var(--orange-text)}
.side-photo{left:276px;top:334px;width:161px;height:173px;padding:5px}
.fill{width:100%;height:100%}
.subscribe{position:absolute;left:276px;top:526px;width:161px;height:110px;background:var(--orange);border-radius:6px;text-align:center;color:#fff;box-shadow:0 6px 8px -4px rgba(0,0,0,.25)}
.subscribe h3{font-family:'Handlee',cursive;font-weight:400;font-size:26px;line-height:36px;margin-top:2px}
.subscribe .field{margin:2px 7px 0;height:23px;background:#fbe6b8;font-size:8px;line-height:23px;color:#c9b58a}
.subscribe .btn{display:inline-block;margin-top:8px;width:78px;height:24px;border-radius:5px;background:#fff;color:var(--orange-text);font-family:'Handlee',cursive;font-size:13px;line-height:24px}
.seen-on{left:276px;top:657px;width:161px;height:199px;text-align:center}
.seen-on h3{font-family:'Handlee',cursive;font-weight:400;font-size:22px;color:var(--teal-text);line-height:30px;margin-top:6px;border-bottom:1px solid #eee;margin-left:14px;margin-right:14px}
.badge{margin:12px auto 0;height:22px;background:#d8d8d8;border-radius:3px}
.tweet{left:276px;top:879px;width:161px;height:109px;padding:14px 8px;font-size:9px;color:#444;line-height:14px}
.tweet .who{font-family:'Handlee',cursive;font-size:11px}
.tweet .date{font-size:6px;margin-bottom:6px}
.hero{left:448px;top:136px;width:496px;height:253px;border-radius:0;padding:0;overflow:hidden}
.hero-photo{position:absolute;left:30px;top:0;width:290px;height:253px}
.hero-name{position:absolute;left:302px;top:160px;font-family:'Handlee',cursive;font-size:24px;color:var(--teal-text)}
.hero-line{position:absolute;left:56px;top:198px;width:330px;text-align:right;font-family:'Handlee',cursive;font-size:13px;line-height:24px;color:var(--orange-text)}
.dots{position:absolute;left:398px;top:229px;display:flex;gap:3px}
.dots i{width:8px;height:8px;border-radius:50%;background:#ddd}
.dots i.on{background:var(--teal)}
.news{position:absolute;left:448px;top:416px;width:496px}
.news h2{font-family:'Handlee',cursive;font-weight:400;font-size:27px;color:var(--teal-text);line-height:34px}
.news p{font-family:'Handlee',cursive;font-style:italic;font-size:12px;line-height:16px;color:#666;margin-top:4px}
.news p+p{margin-top:14px}
.news a{color:var(--link);text-decoration:none}
.videos{left:448px;top:546px;width:496px;height:146px;border-radius:0}
.video{position:absolute;top:3px;height:134px;background:#222}
.video .bar{height:14px;background:#111;color:#eee;font-size:7px;line-height:14px;padding-left:5px}
.video .bar.big{height:26px;font-size:11px;line-height:26px;padding-left:8px}
.play{position:absolute;left:50%;top:50%;width:30px;height:20px;margin:-10px 0 0 -15px;background:#222;border-radius:4px}
.post{left:448px;top:699px;width:496px;height:247px;border-radius:0;padding:0 10px}
.post h2{font-family:'Handlee',cursive;font-weight:400;font-size:26px;color:var(--teal-text);line-height:34px;margin-top:5px}
.post .date{font-size:7px;font-weight:bold;color:var(--orange-text);letter-spacing:.5px;margin:4px 0 6px}
.post p{font-size:7.5px;line-height:11px;color:#777;margin-bottom:8px}
.post .more{position:absolute;left:10px;right:10px;top:212px;border-top:1px solid #ddd;padding-top:6px;font-family:'Handlee',cursive;font-size:12px;color:var(--link)}
.footer{position:absolute;left:0;top:1009px;width:1200px;height:47px;background:linear-gradient(180deg,var(--teal) 0%,var(--teal-light) 100%);color:#fff}
.foot-name{position:absolute;left:275px;top:5px;font-family:'Handlee',cursive;font-size:23px;line-height:26px}
.foot-line{position:absolute;left:275px;top:31px;font-family:'Handlee',cursive;font-size:9px}
.foot-rule{position:absolute;left:563px;top:10px;width:1px;height:28px;background:rgba(255,255,255,.4)}
.social{position:absolute;left:600px;top:15px;display:flex;gap:10px;font-family:'Handlee',cursive;font-size:10px;line-height:16px}
.social span{display:flex;align-items:center;gap:3px}
.social b{width:12px;height:12px;border-radius:50%;background:#fff;opacity:.85}
.legal{position:absolute;right:257px;top:13px;text-align:right;font-size:7.5px;line-height:12px}
</style>
</head>
<body>
<header class="top-band">
  <div class="brand">
    <div class="brand-name">Delia Brunwick</div>
    <div class="brand-line">PROFESSIONAL WRITER. AMATEUR MOM.</div>
  </div>
</header>

<nav class="panel main-nav">
  <a class="current">About Me</a><a>Books</a><a>Articles</a><a>TV</a><a>Hire Me</a><a>Speaking</a><a>Consulting</a><a>Classes</a><a>School Visits</a><a>Press</a><a>Blog</a><a style="border:0">Contact Me</a>
</nav>

<div class="share-note">Share your pictures of your<br>favorite milfs!</div>
<div class="panel side-photo"><div class="fill" role="img" aria-label="Portrait photo of Delia Brunwick" style="background:linear-gradient(160deg,#e8ddd3,#8a5a45 55%,#f1ece8)"></div></div>

<div class="subscribe">
  <h3>Subscribe</h3>
  <div class="field">info@example.com</div>
  <div class="btn">Sign Up</div>
</div>

<div class="panel seen-on">
  <h3>as seen on !</h3>
  <div class="badge" style="width:92px"></div>
  <div class="badge" style="width:92px;background:#c9c9c9"></div>
  <div class="badge" style="width:82px;height:36px"></div>
  <div class="badge" style="width:88px;height:26px"></div>
</div>

<div class="panel tweet">
  <div class="who">Delia Brunwick @DeliaBrunwick</div>
  <div class="date">20 Sep. 2013</div>
  A Guide to Fundraising For Your Kid's School! FANTASTIC! http://lnk.es/q4Tz8 via @pastthebrochure
</div>

<section class="panel hero">
  <div class="hero-photo" role="img" aria-label="Smiling portrait photo of Delia Brunwick" style="background:linear-gradient(180deg,#fff 0%,#e7c9b6 30%,#6b3d2c 70%,#2a2020 100%)"></div>
  <div class="hero-name">Delia Brunwick</div>
  <div class="hero-line">Finding the funny in parenthood before somebody<br>loses an eye.</div>
  <div class="dots"><i class="on"></i><i></i><i></i><i></i></div>
</section>

<section class="news">
  <h2>Latest News !</h2>
  <p>My children's book, "Off to the Splash Zone" is now AVAILABLE in fine book stores (yes...and crappy ones too) everywhere! Read a few of the GREAT reviews <a>HERE!</a>) !</p>
  <p>AndCheck out the book trailer by my oh-so-talented illustrator and friend, Tobin Harlowe (creator of "Poppy and the Grumbly Giant" on Kidloop TV)!!!!</p>
</section>

<section class="panel videos">
  <div class="video" style="left:5px;width:238px">
    <div class="bar">Off to the Splash Zone</div>
    <div role="img" aria-label="Cartoon illustration still from the book trailer" style="height:120px;background:linear-gradient(180deg,#f4f0c8,#e9c784 50%,#5aa3c8)"></div>
    <div class="play"></div>
  </div>
  <div class="video" style="left:251px;width:240px">
    <div class="bar big">Funny Mom - "Need Coffee?" by Delia Brunwick</div>
    <div role="img" aria-label="Video still of Delia Brunwick talking in a bookshop" style="height:108px;background:linear-gradient(90deg,#4a2e24,#7b4a3a 50%,#c9a58f)"></div>
    <div class="play"></div>
  </div>
</section>

<article class="panel post">
  <h2>Co-Sleeping With The Enemy</h2>
  <div class="date">MONDAY, SEPTEMBER 3, 2012</div>
  <p>The "family bed."</p>
  <p>Do you know what this is? It's how psychologists refer to your bed when your children sleep with you. It's the pillow-y haven where the family nestles down together for the night, arms and legs draped across each other in a trusting, completely unprotected fashion. Soft breathing whooshes in and out of your little angels' puckering, lightly parted lips while their dry warm bodies cuddle into your scooping frame and together you recreate the feel of your womb.</p>
  <p>Well, I don't like it.</p>
  <p>And I confirmed this to myself last night when I let my son sleep in my bed.</p>
  <p>I'm not big on co-sleeping. I've never been big on it. I know it works for some people. I however can't have anyone else in my bed. Ever. Even when my boyfriend sleeps over, he is relegated to one side of the bed. If he crosses the line there are consequences. Consequences that usually involve sex being withheld. Or a lot of scowling.</p>
  <div class="more">[ read more ]</div>
</article>

<footer class="footer">
  <div class="foot-name">Delia Brunwick</div>
  <div class="foot-line">Finding the funny in parenthood before somebody loses an eye.</div>
  <div class="foot-rule"></div>
  <div class="social"><span><b></b>Drovely</span><span><b></b>Quenlo</span></div>
  <div class="legal">Copyright 2013. All Right Reserved.<br>Design by Velnor Studio</div>
</footer>
</body>
</html>
```